Business Card Design Project

- makeup artist business card

- original and creative

- Elegant design

- Feel free to come out with cool designs but stick to being elegant and attractive

- Design relates to makeup

- includes name, occupation, contact numbers, email, website

- regular size business card

- round corner card

- double sided

- on 1 side it should just have the website name in the center " velvetbrushhue.com "

Industry/Entity Type

Business

Requirements
Must have
• Marla Tobin
Makeup Artist
USA: +1 (213)555-0147
Singapore: +65 90007312
marlatobin@velvetbrushhue.com
www.velvetbrushhue.com
Should not have
• nothing cartoon looking.
Pictures of makeup being grab from the internet.. Examples: eyes or lips.

```html
<!DOCTYPE html>
<html lang="en">
<head>
<meta charset="utf-8">
<title>Marla Tobin – Makeup Artist Business Card</title>
<link rel="stylesheet" href="https://fonts.googleapis.com/css2?family=Mr+De+Haviland&family=Questrial&display=swap">
<style>
  :root {
    --page-bg: #ececec;
    --card-back: #141414;
    --card-back-edge: #262626;
    --silver: #d9d9d9;
    --card-front: #f6f5f1;
    --card-front-clear: rgba(246, 245, 241, 0);
    --ink: #111111;
    --pink: #f2a9c4;
    --rose: #e58fb0;
    --lilac: #c9b6dc;
    --violet: #a58cc4;
    --script: "Mr De Haviland", cursive;
    --sans: "Questrial", "Century Gothic", sans-serif;
  }

  html, body {
    margin: 0;
    padding: 0;
    width: 1200px;
    height: 1200px;
    overflow: hidden;
    background: var(--page-bg);
  }

  .sheet {
    width: 1200px;
    height: 1200px;
    display: flex;
    flex-direction: column;
    align-items: center;
    justify-content: center;
    gap: 70px;
  }

  .card {
    position: relative;
    width: 840px;
    height: 480px;
    border-radius: 22px;
    overflow: hidden;
    box-shadow: 0 6px 18px rgba(0, 0, 0, 0.18);
  }

  /* Back side: website name centred on black */
  .card--back {
    background: linear-gradient(160deg, var(--card-back-edge), var(--card-back) 55%);
    display: flex;
    align-items: center;
    justify-content: center;
  }

  .back-wordmark {
    margin: 0;
    font-family: var(--script);
    font-weight: 400;
    font-size: 104px;
    line-height: 1;
    color: var(--silver);
    letter-spacing: 1px;
  }

  /* Front side: artwork area left, name and contacts right */
  .card--front {
    background: var(--card-front);
  }

  .front-artwork {
    position: absolute;
    left: 0;
    top: 0;
    width: 400px;
    height: 480px;
    background:
      linear-gradient(90deg, var(--card-front-clear) 50%, var(--card-front) 100%),
      linear-gradient(175deg, var(--violet) 0%, var(--lilac) 35%, var(--pink) 70%, var(--rose) 100%);
  }

  .front-identity {
    position: absolute;
    right: 110px;
    top: 118px;
    text-align: right;
  }

  .front-name {
    margin: 0;
    font-family: var(--script);
    font-weight: 400;
    font-size: 112px;
    line-height: 1;
    color: var(--ink);
  }

  .front-role {
    margin: -6px 0 0;
    font-family: var(--sans);
    font-size: 24px;
    letter-spacing: 1px;
    color: var(--ink);
  }

  .front-contacts {
    position: absolute;
    right: 56px;
    bottom: 44px;
    margin: 0;
    padding: 0;
    list-style: none;
    text-align: right;
    font-family: var(--sans);
    font-size: 25px;
    line-height: 1.32;
    color: var(--ink);
  }
</style>
</head>
<body>
  <main class="sheet">
    <section class="card card--back" aria-label="Card back">
      <p class="back-wordmark">velvetbrushhue.com</p>
    </section>

    <section class="card card--front" aria-label="Card front">
      <div class="front-artwork" role="img" aria-label="Painterly makeup illustration in pink, violet and teal tones"></div>

      <div class="front-identity">
        <h1 class="front-name">Marla Tobin</h1>
        <p class="front-role">MAKEUP ARTIST</p>
      </div>

      <ul class="front-contacts">
        <li class="contact-phone">USA: +1 (213)555-0147</li>
        <li class="contact-phone">Singapore: +65 90007312</li>
        <li class="contact-email">marlatobin@velvetbrushhue.com</li>
        <li class="contact-web">www.velvetbrushhue.com</li>
      </ul>
    </section>
  </main>
</body>
</html>
```